KettlesArmsPersonal

I am a cutting edge, top of the line gun store. We are expanding faster than we can keep up. We offer: Gunsmithing, Transfers, Concealed Carry, Machine Guns, Suppressors. My colors are reflected in my logo. Red, black and white. I like a clean design that gets the point across. I was trying to find a plastic business card, but will settle with a high quality paper product.

Industry/Entity Type

Plastic

Contact Information for Business Card

Dwayne Kettle - Owner
620-555-0148 (Cell)
Kettle's Arms Outfitters
4117 E. Hwy 9
Healy, KS 67099
sales@kettlesarmsoutfitters.example
kettlesarmsoutfitters.example

```html
<!DOCTYPE html>
<html lang="en">
<head>
<meta charset="utf-8">
<title>Kettle's Arms Outfitters – Business Card</title>
<link rel="stylesheet" href="https://fonts.googleapis.com/css2?family=Exo+2:wght@400;500;700;800&display=swap">
<style>
  :root {
    --backdrop: #a8a8a8;
    --card: #ffffff;
    --ink: #111111;
    --text: #2a2a2a;
    --muted: #555555;
    --accent: #8e1418;
    --font: "Exo 2", sans-serif;
  }
  * { box-sizing: border-box; margin: 0; padding: 0; }
  html, body { width: 1200px; height: 895px; overflow: hidden; }
  body {
    background: var(--backdrop);
    font-family: var(--font);
    position: relative;
  }
  .card {
    position: absolute;
    width: 540px;
    height: 309px;
    background: var(--card);
    overflow: hidden;
  }
  .card svg.bands { position: absolute; inset: 0; }
  .card--front { left: 610px; top: 110px; }
  .card--back  { left: 50px;  top: 476px; }

  .brand {
    position: absolute;
    display: flex;
    align-items: center;
    gap: 10px;
    color: var(--ink);
    font-weight: 800;
    text-transform: uppercase;
    letter-spacing: 1px;
    white-space: nowrap;
  }
  .brand__dot { border-radius: 50%; background: var(--accent); flex: none; }
  .card--front .brand { left: 0; right: 0; top: 134px; justify-content: center; font-size: 28px; }
  .card--front .brand__dot { width: 26px; height: 26px; }
  .card--back .brand { left: 60px; top: 24px; font-size: 17px; }
  .card--back .brand__dot { width: 16px; height: 16px; }

  .text { position: absolute; color: var(--text); font-weight: 500; white-space: nowrap; }
  .contact-web { left: 16px; top: 106px; font-size: 11px; line-height: 15px; }
  .contact-address { left: 250px; top: 160px; font-size: 13px; line-height: 18px; }
  .contact-phone { left: 404px; top: 214px; font-size: 14px; line-height: 19px; font-weight: 700; letter-spacing: 0.5px; }
  .person { position: absolute; right: 20px; top: 80px; text-align: right; }
  .person__name { font-size: 19px; font-weight: 700; letter-spacing: 1.5px; color: var(--text); text-transform: uppercase; line-height: 22px; }
  .person__title { font-size: 9px; font-weight: 700; letter-spacing: 1px; color: var(--muted); text-transform: uppercase; margin-top: 1px; }
</style>
</head>
<body>

<section class="card card--front" aria-label="Card front">
  <svg class="bands" width="540" height="309" viewBox="0 0 540 309">
    <polygon fill="#111" points="0,0 540,0 540,42 390,42 366,70 174,70 150,42 0,42"/>
    <polyline fill="none" stroke="#8e1418" stroke-width="3" points="150,46 172,72"/>
    <polyline fill="none" stroke="#8e1418" stroke-width="3" points="390,46 368,72"/>
    <polygon fill="#111" points="0,309 540,309 540,267 390,267 366,239 174,239 150,267 0,267"/>
    <polyline fill="none" stroke="#8e1418" stroke-width="3" points="150,263 172,237"/>
    <polyline fill="none" stroke="#8e1418" stroke-width="3" points="390,263 368,237"/>
  </svg>
  <div class="brand"><span class="brand__dot"></span>Kettle's Arms Outfitters</div>
</section>

<section class="card card--back" aria-label="Card back">
  <svg class="bands" width="540" height="309" viewBox="0 0 540 309">
    <polygon fill="#111" points="0,66 178,66 196,83 178,100 0,100"/>
    <polyline fill="none" stroke="#8e1418" stroke-width="3" points="184,66 202,83 184,100"/>
    <polygon fill="#111" points="240,118 372,118 390,135 372,152 240,152"/>
    <polyline fill="none" stroke="#8e1418" stroke-width="3" points="378,118 396,135 378,152"/>
    <rect x="404" y="170" width="136" height="34" fill="#111"/>
    <rect x="0" y="258" width="540" height="4" fill="#8e1418"/>
    <rect x="0" y="266" width="540" height="43" fill="#111"/>
    <g fill="none" stroke="#fff" stroke-width="1.6">
      <circle cx="40" cy="83" r="10"/>
      <ellipse cx="40" cy="83" rx="4.5" ry="10"/>
      <line x1="30" y1="83" x2="50" y2="83"/>
      <line x1="32" y1="77" x2="48" y2="77"/>
      <line x1="32" y1="89" x2="48" y2="89"/>
    </g>
    <path fill="#fff" d="M310 125a8 8 0 0 1 8 8c0 6-8 14-8 14s-8-8-8-14a8 8 0 0 1 8-8z"/>
    <circle cx="310" cy="133" r="3" fill="#111"/>
    <g fill="none" stroke="#fff" stroke-width="1.8">
      <rect x="466" y="176" width="13" height="22" rx="2"/>
      <line x1="470" y1="194" x2="475" y2="194"/>
    </g>
  </svg>

  <div class="brand"><span class="brand__dot"></span>Kettle's Arms Outfitters</div>

  <div class="person">
    <p class="person__name">Dwayne Kettle</p>
    <p class="person__title">Owner</p>
  </div>

  <p class="text contact-web">sales@kettlesarmsoutfitters.example<br>kettlesarmsoutfitters.example</p>
  <p class="text contact-address">4117 E. Hwy 9<br>Healy, KS 67099</p>
  <p class="text contact-phone">620-555-0148</p>
</section>

</body>
</html>
```